High end boutique food product label

We are looking for a label design to be used on our range of high end food products. We don't have a design or colour scheme in mind and are interested to see what ideas are submitted.
We would like it to feel sophisticated, chic, and eye-catching.
All of our products are handmade in Australia using Australian ingredients.
The graphics for the label will need to be scaleable to be fit a variety of labels from small squat jars with labels sized 3.5cm high and 7cm wide, to tall thin bottles with labels that are 14cm high and 4.5cm wide.
We would be interested in working with the winning designer to create these different sized labels.
The label submitted for this project should be 14cm high and 4.5cm wide, it should include our logo (file supplied in .jpeg and .ai), the product name 'Extra Virgin Olive Oil' and the size '250ml'.
This is just the front label on a bottle, we are not expecting a rear label to be created currently.
You are welcome to use any fonts you think will look good but the fonts used in our logo are Allaina Medium and Bebas Kai Regular.

```html
<!DOCTYPE html>
<html lang="en">
<head>
<meta charset="utf-8">
<title>Wren Pantry – Extra Virgin Olive Oil Labels</title>
<link rel="stylesheet" href="https://fonts.googleapis.com/css2?family=Rye&family=Cinzel:wght@900&family=Playfair+Display:wght@400&family=Oswald:wght@300&display=swap">
<style>
  :root {
    --olive: #364220;
    --olive-deep: #2b3519;
    --ribbon: #45291a;
    --tan: #bba88a;
    --cream: #efe7d6;
    --white: #ffffff;
    --brand-red: #9b1b27;
    --page: #ffffff;
  }
  * { margin: 0; padding: 0; box-sizing: border-box; }
  html, body { width: 686px; height: 1200px; overflow: hidden; background: var(--page); }
  .canvas { position: relative; width: 686px; height: 1200px; }

  .label { position: absolute; display: block; }
  .label--wide { left: 23px; top: 24px; width: 640px; height: 320px; }
  .label--tall { left: 23px; top: 364px; width: 263px; height: 816px; }

  .brand-tile {
    position: absolute; left: 340px; top: 364px; width: 250px; height: 346px;
    background: var(--brand-red);
    display: flex; flex-direction: column; align-items: center; justify-content: center;
    font-family: "Playfair Display", Georgia, serif; font-weight: 400; color: var(--cream);
    font-size: 46px; line-height: 1.1; text-align: center;
  }

  .t-headline { font-family: "Rye", Georgia, serif; fill: var(--tan); }
  .t-banner { font-family: "Cinzel", Georgia, serif; font-weight: 900; fill: var(--white); }
  .t-size { font-family: "Playfair Display", Georgia, serif; font-weight: 400; fill: var(--white); }
  .t-brand { font-family: "Playfair Display", Georgia, serif; font-weight: 400; fill: var(--cream); }
  .t-copy { font-family: "Oswald", Arial, sans-serif; font-weight: 300; fill: var(--cream); letter-spacing: 0.5px; }
</style>
</head>
<body>
<main class="canvas">

  <!-- Wide jar label -->
  <svg class="label label--wide" viewBox="0 0 957 478" aria-label="Extra Virgin Olive Oil jar label">
    <rect class="label__ground" width="957" height="478" fill="var(--olive)"/>
    <path class="label__frame" d="M214,23 H882 L935,76 V402 L880,456 H82 L30,404 V280" fill="none" stroke="var(--white)" stroke-width="3"/>
    <line class="label__dots" x1="230" y1="40" x2="862" y2="40" stroke="var(--white)" stroke-width="6" stroke-linecap="round" stroke-dasharray="0 19"/>
    <line class="label__dots" x1="92" y1="440" x2="872" y2="440" stroke="var(--white)" stroke-width="6" stroke-linecap="round" stroke-dasharray="0 19"/>

    <polygon class="label__ribbon" points="32,0 214,0 214,265 123,228 32,265" fill="var(--ribbon)"/>
    <text class="t-brand" x="123" y="150" font-size="32" text-anchor="middle">Wren</text>
    <text class="t-brand" x="123" y="188" font-size="32" text-anchor="middle">Pantry</text>

    <circle class="label__badge" cx="128" cy="330" r="32" fill="var(--olive-deep)" stroke="var(--tan)" stroke-width="3"/>

    <text class="t-headline" x="478" y="176" font-size="108" text-anchor="middle" textLength="322" lengthAdjust="spacingAndGlyphs">EXTRA</text>
    <text class="t-headline" x="478" y="278" font-size="108" text-anchor="middle" textLength="336" lengthAdjust="spacingAndGlyphs">VIRGIN</text>

    <path class="label__banner" d="M258,300 Q478,285 700,300 L692,385 Q478,378 266,385 Z" fill="none" stroke="var(--tan)" stroke-width="4"/>
    <text class="t-banner" x="480" y="366" font-size="50" text-anchor="middle" textLength="330" lengthAdjust="spacingAndGlyphs">OLIVE OIL</text>

    <polygon class="label__size-box" points="356,400 600,400 613,429 600,458 356,458 343,429" fill="var(--olive-deep)" stroke="var(--tan)" stroke-width="3"/>
    <text class="t-size" x="478" y="442" font-size="36" text-anchor="middle">250ml</text>

    <circle cx="796" cy="215" r="110" fill="var(--white)"/>
    <circle cx="796" cy="215" r="101" fill="none" stroke="var(--olive)" stroke-width="3"/>
    <circle cx="796" cy="215" r="92" fill="var(--cream)" role="img" aria-label="Line drawing of two olives on a leafy sprig"/>
  </svg>

  <!-- Tall bottle label -->
  <svg class="label label--tall" viewBox="0 0 385 1195" aria-label="Extra Virgin Olive Oil bottle label">
    <rect class="label__ground" width="385" height="1195" fill="var(--olive)"/>
    <line x1="14" y1="60" x2="14" y2="1135" stroke="var(--white)" stroke-width="5" stroke-linecap="round" stroke-dasharray="0 17"/>
    <line x1="371" y1="60" x2="371" y2="1135" stroke="var(--white)" stroke-width="5" stroke-linecap="round" stroke-dasharray="0 17"/>
    <line x1="30" y1="80" x2="30" y2="1110" stroke="var(--white)" stroke-width="2.5"/>
    <line x1="355" y1="80" x2="355" y2="1110" stroke="var(--white)" stroke-width="2.5"/>
    <line x1="110" y1="1180" x2="280" y2="1180" stroke="var(--white)" stroke-width="5" stroke-linecap="round" stroke-dasharray="0 13"/>

    <polygon class="label__ribbon" points="116,0 268,0 268,220 192,198 116,220" fill="var(--ribbon)"/>
    <text class="t-brand" x="192" y="128" font-size="28" text-anchor="middle">Wren</text>
    <text class="t-brand" x="192" y="162" font-size="28" text-anchor="middle">Pantry</text>

    <polygon class="label__bar" points="142,222 192,206 242,222 242,545 142,545" fill="var(--tan)"/>

    <circle cx="191" cy="377" r="112" fill="var(--white)"/>
    <circle cx="191" cy="377" r="103" fill="none" stroke="var(--olive)" stroke-width="3"/>
    <circle cx="191" cy="377" r="94" fill="var(--cream)" role="img" aria-label="Line drawing of two olives on a leafy sprig"/>

    <text class="t-headline" x="191" y="636" font-size="96" text-anchor="middle" textLength="270" lengthAdjust="spacingAndGlyphs">EXTRA</text>
    <text class="t-headline" x="191" y="726" font-size="96" text-anchor="middle" textLength="283" lengthAdjust="spacingAndGlyphs">VIRGIN</text>

    <path class="label__banner" d="M10,760 Q191,745 375,760 L369,832 Q191,822 16,832 Z" fill="none" stroke="var(--tan)" stroke-width="3.5"/>
    <text class="t-banner" x="192" y="812" font-size="42" text-anchor="middle" textLength="270" lengthAdjust="spacingAndGlyphs">OLIVE OIL</text>

    <text class="t-copy" x="192" y="882" font-size="21" text-anchor="middle">LOREM IPSUM DOLOR SIT</text>
    <text class="t-copy" x="192" y="908" font-size="21" text-anchor="middle">AMET, CONSECTETUER</text>
    <text class="t-copy" x="192" y="934" font-size="21" text-anchor="middle">ADIPISCING ELIT, SED DIAM</text>
    <text class="t-copy" x="192" y="960" font-size="21" text-anchor="middle">NONUMMY NIBH EUISMOD</text>

    <polygon class="label__size-box" points="120,993 266,993 277,1011 266,1029 120,1029 109,1011" fill="none" stroke="var(--tan)" stroke-width="2.5"/>
    <text class="t-size" x="193" y="1020" font-size="24" text-anchor="middle">250ml</text>

    <circle class="label__badge" cx="191" cy="1080" r="26" fill="var(--olive-deep)" stroke="var(--tan)" stroke-width="2.5"/>
  </svg>

  <!-- Brand tile -->
  <div class="brand-tile">
    <span>Wren</span>
    <span>Pantry</span>
  </div>

</main>
</body>
</html>
```